Velvet Moth Studio Menu

I am the owner of a brand new eyelash & skincare studio called Velvet Moth Studio in Aliso Viejo, CA. I have a lot of services that I offer and I would like to make my menu very simple and easy to read not cluttered at all. My inspirations are Poiret, Lumo, Grove Pallor, KIV, Fern Loft, ect. I love simplicity but artistic. My company colors are black, white, grey, and coral. I have attached all of my services and pricing. My facials have a lot of description in them, if you choose to re-word that or delete wording thats totally fine. I am looking for someone to really be creative with this. Thank you!!! This is my website also: www.velvetmothstudio.example

Target Market(s)

Women ages 18-40

Industry/Entity Type

It Company

Font styles to use
Serif
Sans Serif
Script

Colors
f59195
f04a50
cbcbcb
c4c4c4
b1b1b1
1b1b1b
5c5c5c
ffffff

Requirements
Should not have
• Clutter

```html
<!DOCTYPE html>
<html lang="en">
<head>
<meta charset="utf-8">
<title>Velvet Moth Studio</title>
<link rel="stylesheet" href="https://fonts.googleapis.com/css2?family=Lustria&display=swap">
<style>
  :root {
    --ink: #000000;
    --paper: #ffffff;
    --coral: #f04a50;
    --coral-soft: #e8505a;
    --charcoal: #1b1b1b;
    --sand: #c9b8a4;
    --sea: #b9c4c8;
  }
  html, body {
    margin: 0;
    padding: 0;
    width: 1200px;
    height: 856px;
    overflow: hidden;
    background: var(--ink);
  }
  .canvas {
    position: relative;
    width: 1200px;
    height: 856px;
    background: var(--ink);
    font-family: "Lustria", Georgia, serif;
    overflow: hidden;
  }
  .backdrop {
    position: absolute;
    inset: 0;
  }
  .centered {
    position: absolute;
    transform: translateX(-50%);
    text-align: center;
    white-space: nowrap;
    margin: 0;
  }
  .address {
    left: 605px;
    top: 86px;
    color: var(--coral);
    font-size: 20px;
    line-height: 24px;
  }
  .brand-name {
    position: absolute;
    transform: translate(-50%, -50%);
    text-align: center;
    color: var(--charcoal);
    text-transform: uppercase;
    line-height: 1.05;
    margin: 0;
    font-weight: 400;
  }
  .brand-name--small {
    left: 603px;
    top: 292px;
    font-size: 25px;
    letter-spacing: 2px;
  }
  .brand-name--large {
    left: 985px;
    top: 280px;
    font-size: 42px;
    letter-spacing: 3px;
  }
  .contact {
    position: absolute;
    display: flex;
    align-items: center;
    gap: 8px;
    color: var(--coral);
    font-size: 19px;
    margin: 0;
  }
  .contact--phone { left: 510px; top: 426px; }
  .contact--email { left: 420px; top: 455px; font-size: 17px; gap: 18px; }
  .contact svg { display: block; }
  .section-title {
    color: var(--paper);
    font-size: 23px;
    font-weight: 400;
  }
  .section-body {
    color: var(--paper);
    font-size: 19px;
    line-height: 20px;
  }
  .gift-title { left: 206px; top: 588px; }
  .gift-text { left: 204px; top: 636px; }
  .gift-url { left: 204px; top: 696px; font-size: 19px; color: var(--paper); }
  .hours-title { left: 596px; top: 588px; }
  .hours-text { left: 596px; top: 649px; line-height: 25px; }
  .social {
    position: absolute;
    left: 432px;
    top: 786px;
    display: flex;
    align-items: center;
    gap: 12px;
    margin: 0;
    color: var(--coral);
    font-size: 16px;
  }
  .social-dots {
    display: flex;
    gap: 13px;
    margin-left: 4px;
  }
  .social-dot {
    width: 20px;
    height: 20px;
    border-radius: 50%;
    background: var(--coral);
  }
  .footer-url {
    position: absolute;
    left: 842px;
    top: 790px;
    margin: 0;
    color: var(--paper);
    font-size: 15px;
    letter-spacing: 2px;
  }
</style>
</head>
<body>
<main class="canvas">
  <svg class="backdrop" width="1200" height="856" viewBox="0 0 1200 856" aria-hidden="true">
    <defs>
      <clipPath id="panel-clip">
        <path d="M0,330 C150,230 330,110 520,75 C750,35 1000,28 1200,28 L1200,415 C1080,520 900,570 720,568 C560,565 480,510 330,497 C200,488 80,505 0,522 Z"/>
      </clipPath>
      <linearGradient id="beach-tones" x1="0" y1="0" x2="0" y2="1">
        <stop offset="0" stop-color="#d8dde0"/>
        <stop offset="0.42" stop-color="#b9c4c8"/>
        <stop offset="0.55" stop-color="#cfd3d2"/>
        <stop offset="0.75" stop-color="#c9b8a4"/>
        <stop offset="1" stop-color="#b8a690"/>
      </linearGradient>
    </defs>
    <path class="coral-band" fill="#e8505a" d="M0,312 C150,214 330,96 520,64 C750,30 1000,24 1200,24 L1200,400 L1200,432 C1080,540 900,584 720,582 C560,580 480,524 330,510 C200,500 80,515 0,538 Z"/>
    <path class="white-panel" fill="#ffffff" d="M0,330 C150,230 330,110 520,75 C750,35 1000,28 1200,28 L1200,415 C1080,520 900,570 720,568 C560,565 480,510 330,497 C200,488 80,505 0,522 Z"/>
    <rect clip-path="url(#panel-clip)" x="0" y="60" width="396" height="480" fill="url(#beach-tones)" role="img" aria-label="Photo of a woman with long blonde hair in a pink bikini standing on a beach facing the sea"/>
  </svg>

  <p class="centered address">18 Larkspur Row<br>Aliso Viejo, CA 92656</p>

  <h2 class="brand-name brand-name--small">Velvet Moth<br>Studio</h2>
  <h1 class="brand-name brand-name--large">Velvet Moth<br>Studio</h1>

  <p class="contact contact--phone">
    <svg width="20" height="20" viewBox="0 0 24 24" aria-hidden="true"><path fill="#000" d="M6.6 10.8c1.4 2.8 3.8 5.1 6.6 6.6l2.2-2.2c.3-.3.7-.4 1-.2 1.1.4 2.3.6 3.6.6.6 0 1 .4 1 1V20c0 .6-.4 1-1 1C10.6 21 3 13.4 3 4c0-.6.4-1 1-1h3.5c.6 0 1 .4 1 1 0 1.3.2 2.5.6 3.6.1.3 0 .7-.2 1L6.6 10.8z"/></svg>
    (949) 555-0142
  </p>
  <p class="contact contact--email">
    <svg width="22" height="16" viewBox="0 0 22 16" aria-hidden="true"><rect x="1" y="1" width="20" height="14" fill="none" stroke="#000" stroke-width="2"/><path d="M1 1 L11 9 L21 1 M1 15 L8 7 M21 15 L14 7" fill="none" stroke="#000" stroke-width="2"/></svg>
    hello@velvetmothstudio.example
  </p>

  <h3 class="centered section-title gift-title">A Gift of Beauty</h3>
  <p class="centered section-body gift-text">Gift vouchers can be purchased on<br>our website.</p>
  <p class="centered gift-url">www.velvetmothstudio.example</p>

  <h3 class="centered section-title hours-title">Opening Hours</h3>
  <p class="centered section-body hours-text">M-F&nbsp; 8.00am – 9.00pm<br>Sat- Sun 9.00am – 6.00pm</p>

  <p class="social">Find us on
    <span class="social-dots">
      <span class="social-dot"></span>
      <span class="social-dot"></span>
      <span class="social-dot"></span>
      <span class="social-dot"></span>
      <span class="social-dot"></span>
      <span class="social-dot"></span>
      <span class="social-dot"></span>
    </span>
  </p>

  <p class="footer-url">www.velvetmothstudio.example</p>
</main>
</body>
</html>
```